Broschüren-Design für Produzent von hochwertigen Verpackungs- und Präsentationslösungen
Zielgruppe
Wir produzieren hochwertige Verpackungs- und Präsentationslösungen.
Unsere Zielgruppe sind Firmen, welche kreative Premium-Packaging benötigt.
Aufgabenstellung
- Format: A4 hoch
- Umfang: 6 Seiten
- Falzart: Wickelfalz
- Design muss sehr hochwertig sein. Passend zu unseren Produktion (siehe Bilder)
- Wir möchten mit diesem Falzprospekt eine Übersicht über unsere Produkte generieren.
- Die Produkte sind bereits schon hochwertig fotografiert und müssen in einem anspruchsvollen Design in Szene gesetzt werden.
- Der Prospekt sollte die Kunden emotional berühren.
- Auf der Titelseite werden wir den Titel «High Performance Packaging» mit Folien prägen
- Seitenaufbau gemäss meiner Visualisierung (im Anhang)
- Bei jeder Produktkategorie möchte ich ein Grosses Übersichtsbild zusammen mit einem kurzen Text.
Ergänzend können noch weitere (passende) Bilder der jeweiligen Kategorie abgebildet werden.
Im Anhang finden Sie:
- Visualisierung des zu gestaltenden Prospekt
- Werbeflyer (zur Ansicht/Inspiration). In etwa so stellen wir uns das Design/Tonalität vor.
- Weitere passende Produktbilder können vorerst auf der Webseite unseres Produktionspartner (www.bogenhaus.de) entnommen werden.

```html
<!DOCTYPE html>
<html lang="de">
<head>
<meta charset="utf-8">
<title>High Performance Packaging – Wickelfalz-Prospekt</title>
<link rel="stylesheet" href="https://fonts.googleapis.com/css2?family=Playfair+Display:ital,wght@1,800;1,900&family=IBM+Plex+Sans:wght@400;600&display=swap">
<style>
:root{
  --navy:#3a3f4d;
  --navy-deep:#2c303b;
  --copper:#c97d4e;
  --paper:#ffffff;
  --mist:#e4e4e8;
  --stage:#d8d7d5;
  --ink:#2f333d;
  --muted:#6b6f79;
  --soft:#c9ccd4;
}
*{box-sizing:border-box;margin:0;padding:0}
html,body{width:848px;height:1200px;overflow:hidden}
body{background:var(--stage);font-family:"IBM Plex Sans",Arial,sans-serif;color:var(--ink);position:relative}
.spread{position:absolute;left:24px;width:800px;height:377px;display:flex;box-shadow:0 1px 3px rgba(0,0,0,.15)}
.spread--inside{top:190px}
.spread--outside{top:607px}
.panel{position:relative;width:266.67px;height:377px;overflow:hidden;background:var(--paper)}
.panel + .panel{border-left:1px solid rgba(0,0,0,.08)}
.panel--navy{background:var(--navy)}
.band{position:absolute;left:0;width:100%;height:125.7px;overflow:hidden}
.band--navy{background:var(--navy);color:#fff}
.band--paper{background:var(--paper)}
.band--1{top:0}.band--2{top:125.7px}.band--3{top:251.3px}
.cat-title{position:absolute;left:12px;top:12px;font-family:"Playfair Display",Georgia,serif;font-style:italic;font-weight:900;font-size:10.5px;letter-spacing:.2px}
.cat-text{position:absolute;left:12px;top:30px;width:100px;font-size:4.6px;line-height:7px;opacity:.85}
.band--paper .cat-text{color:var(--muted);opacity:1}
.photo{position:absolute}
.photo--boxes{left:110px;top:34px;width:148px;height:80px;background:linear-gradient(135deg,#2a2c33 0%,#1b1c21 40%,#a9905e 62%,#6c6f78 100%);clip-path:polygon(8% 70%,40% 55%,55% 20%,98% 30%,88% 85%,20% 98%)}
.photo--slipcase{left:148px;top:8px;width:60px;height:110px;background:linear-gradient(90deg,#b7bac3 0 40%,#1f2026 40% 100%)}
.photo--samples{left:90px;top:42px;width:176px;height:84px;background:linear-gradient(160deg,#1d1e22 0%,#2a2b30 45%,#c9a992 65%,#eceae7 100%);clip-path:polygon(30% 0,100% 20%,100% 100%,0 100%)}
.photo--binder{left:80px;top:36px;width:150px;height:80px;background:linear-gradient(150deg,#d72e3d 0 30%,#e7e8ec 30% 75%,#a7aab3 100%);clip-path:polygon(55% 0,100% 25%,45% 100%,0 55%)}
.photo--case{left:12px;top:12px;width:194px;height:100px;background:linear-gradient(180deg,#d3d5da 0%,#f3f3f4 55%,#8f9299 100%)}
.photo--fan{left:160px;top:10px;width:100px;height:108px;background:linear-gradient(200deg,#4c505b 0%,#2d3038 70%);clip-path:polygon(35% 0,100% 10%,100% 100%,20% 85%)}
.photo--folder{left:140px;top:34px;width:126px;height:86px;background:linear-gradient(160deg,#eef0f3 0%,#bfc3cb 60%,#8c909a 100%);clip-path:polygon(0 35%,100% 0,100% 75%,10% 100%)}
.photo--clip{left:100px;top:56px;width:166px;height:70px;background:linear-gradient(160deg,#fafafa 0%,#e2e3e6 70%,#9fa2aa 100%);clip-path:polygon(40% 100%,100% 0,100% 100%)}
.showcase{position:absolute;left:12px;top:138px;width:242px;height:224px;background:var(--mist)}
.showcase .cat-title{top:128px;left:20px;color:var(--ink)}
.showcase .cat-text{top:146px;left:20px;width:160px;color:var(--muted)}
.badge{position:absolute;border-radius:50%;background:var(--copper);color:var(--navy-deep);font-family:"Playfair Display",Georgia,serif;font-style:italic;font-weight:900;text-align:center;display:flex;align-items:center;justify-content:center;transform:rotate(-12deg)}
.badge--small{left:138px;top:60px;width:38px;height:38px;font-size:6px;line-height:6.5px}
.badge--cover{left:207px;top:26px;width:50px;height:50px;font-size:7.5px;line-height:8px}
/* outside */
.intro{position:absolute;left:20px;top:26px;width:200px}
.intro h2{font-size:8.4px;line-height:10px;font-weight:600;margin-bottom:8px}
.intro p{font-size:4.4px;line-height:6.6px;color:var(--muted);margin-bottom:4px}
.eco{position:absolute;left:20px;top:140px;width:204px;height:220px;background:var(--mist);padding:12px 12px}
.eco h3{font-size:6px;font-weight:600;margin-bottom:5px}
.eco>p{font-size:4.4px;line-height:6.6px;color:var(--muted);width:150px;margin-bottom:14px}
.eco-item{display:flex;gap:10px;margin-bottom:12px;align-items:flex-start}
.eco-icon{flex:none;width:18px;height:18px}
.eco-item h4{font-size:4.6px;font-weight:600;margin-bottom:2px}
.eco-item p{font-size:4.2px;line-height:6.2px;color:var(--muted);width:120px}
.imprint{position:absolute;left:60px;bottom:38px;display:flex;gap:10px;align-items:flex-end;color:#fff}
.brand-name{font-size:11px;font-weight:600;line-height:1}
.contact{font-size:4.2px;line-height:6.4px;opacity:.9}
.contact strong{font-weight:600}
.contact .owner{margin-top:6px}
.cover-photo{position:absolute;left:18px;top:80px;width:248px;height:132px;background:linear-gradient(120deg,#262830 0 18%,#7a5a46 18% 40%,#3a3e49 40% 55%,#a7abb6 55% 85%,#2b2e36 85%)}
.cover-title{position:absolute;left:18px;top:234px;font-family:"Playfair Display",Georgia,serif;font-style:italic;font-weight:900;font-size:17.5px;line-height:21px;color:var(--copper)}
.cover-sub{position:absolute;left:18px;top:349px;font-size:4.8px;color:#dfe1e6}
</style>
</head>
<body>

<section class="spread spread--inside" aria-label="Innenseiten">
  <div class="panel">
    <div class="band band--navy band--1">
      <h3 class="cat-title">Verpackungen</h3>
      <p class="cat-text">Ma eos magnam nonem estibust laborerum ates alia dolupta sperarum quisti berum explanimil eleseti latquas.</p>
      <div class="photo photo--boxes" role="img" aria-label="Produktfoto: schwarze und goldene Verpackungsboxen mit Magnetdeckel"></div>
    </div>
    <div class="band band--paper band--2">
      <h3 class="cat-title">Schuber</h3>
      <p class="cat-text">Ma eos magnam nonem estibust laborerum ates alia dolupta sperarum quisti berum explanimil eleseti latquas. Obit mi, esto doluptis di solent experum et a aut odis alis quibus voluptate plicide repellectem dellat illuscipit, in cus eatesenae non cor sanim.</p>
      <div class="photo photo--slipcase" role="img" aria-label="Produktfoto: schwarzer Schuber mit drei grauen Ordnern"></div>
    </div>
    <div class="band band--navy band--3">
      <h3 class="cat-title">Mustermappen</h3>
      <p class="cat-text">Ma eos magnam nonem estibust laborerum ates alia dolupta sperarum quisti explanimil eleseti latquas.</p>
      <div class="photo photo--samples" role="img" aria-label="Produktfoto: schwarze Mustermappe mit Farbmustern"></div>
    </div>
  </div>

  <div class="panel">
    <div class="band band--navy band--1">
      <h3 class="cat-title">Ringordner</h3>
      <p class="cat-text">Ma eos magnam nonem estibust laborerum ates alia dolupta sperarum quisti berum explanimil eleseti latquas.</p>
      <div class="photo photo--binder" role="img" aria-label="Produktfoto: geöffneter Ringordner mit roter Kante"></div>
    </div>
    <div class="showcase">
      <div class="photo photo--case" role="img" aria-label="Produktfoto: weisser Präsentationskoffer mit Einlage"></div>
      <h3 class="cat-title">Präsentationskoffer</h3>
      <p class="cat-text">Ma eos magnam nonem estibust laborerum ates alia dolupta sperarum quisti berum explanimil eleseti latquas dolupta sperarum quisti.</p>
    </div>
  </div>

  <div class="panel">
    <div class="band band--navy band--1">
      <h3 class="cat-title">Fächermappen</h3>
      <p class="cat-text">Ma eos magnam nonem estibust laborerum ates alia dolupta sperarum quisti berum explanimil eleseti latquas dolupta.</p>
      <div class="photo photo--fan" role="img" aria-label="Produktfoto: graue Fächermappe, aufgestellt"></div>
      <div class="badge badge--small">Exklusiv<br>und hoch<br>wertig</div>
    </div>
    <div class="band band--paper band--2">
      <h3 class="cat-title">Präsentationsmappen</h3>
      <p class="cat-text">Ma eos magnam nonem estibust laborerum ates alia dolupta sperarum quisti eleseti magnam.</p>
      <div class="photo photo--folder" role="img" aria-label="Produktfoto: geöffnete graue Präsentationsmappe mit Ringmechanik"></div>
    </div>
    <div class="band band--navy band--3">
      <h3 class="cat-title">Schreibmappen</h3>
      <p class="cat-text">Ma eos magnam nonem estibust laborerum ates alia dolupta sperarum quisti explanimil eleseti latquas.</p>
      <div class="photo photo--clip" role="img" aria-label="Produktfoto: Schreibmappe mit Klemme und Stift"></div>
    </div>
  </div>
</section>

<section class="spread spread--outside" aria-label="Aussenseiten">
  <div class="panel">
    <div class="intro">
      <h2>Höchste Qualität<br>zu unschlagbaren Preisen.</h2>
      <p>Mit einer unvergleichlich grossen Bandbreite im Bereich des Arvenpack bieten wir vielseitige Verpackungs- und Präsentationslösungen.</p>
      <p>Einzigartiges Design, variable Formen und hochwertige Haptik unterstreichen die Bedeutung von Ihren Produkten.</p>
      <p>Überzeugen Sie sich jetzt und bestellen Sie Ihr individuelles Angebot!</p>
    </div>
    <div class="eco">
      <h3>Nachhaltige Papiere als Standard</h3>
      <p>Bei uns gehen neuste Technologien und Umweltschutz Hand in Hand. Wir setzen auf nachhaltige Materialien und eine emissionsarme Produktion.</p>
      <div class="eco-item">
        <svg class="eco-icon" viewBox="0 0 18 18" aria-hidden="true"><circle cx="9" cy="9" r="9" fill="#fff"/><path d="M6 13V9M6 9l-2 2M6 9l2 2M6 5l-2.5 4h5zM12 13V8M12 4l-3 5h6z" stroke="#2f7a4a" stroke-width="1" fill="#2f7a4a"/></svg>
        <div><h4>Nachhaltige Papiere</h4><p>Unsere Rohstoffe stammen aus nachhaltiger Forstwirtschaft.</p></div>
      </div>
      <div class="eco-item">
        <svg class="eco-icon" viewBox="0 0 18 18" aria-hidden="true"><circle cx="9" cy="9" r="9" fill="#fff"/><path d="M9 4l4 1.5v3.5c0 2.5-2 4-4 5-2-1-4-2.5-4-5V5.5z" fill="#2f7a4a"/></svg>
        <div><h4>Wiederverwendbarkeit</h4><p>Unsere Boxen sind so schön und stabil, dass man sie auf jeden Fall wiederverwendet.</p></div>
      </div>
      <div class="eco-item">
        <svg class="eco-icon" viewBox="0 0 18 18" aria-hidden="true"><circle cx="9" cy="9" r="9" fill="#fff"/><path d="M9 4.5l2 3.2M12.8 10l-1.8 3.3H7.2M5.2 10l1.8-3" stroke="#2f7a4a" stroke-width="1.3" fill="none"/></svg>
        <div><h4>Recyclebare Lösungen</h4><p>Auf Nachfrage können wir Ihnen eine 100% recyclebare Verpackung anbieten.</p></div>
      </div>
    </div>
  </div>

  <div class="panel panel--navy">
    <div class="imprint">
      <div class="brand-name">Arvenpack</div>
      <div class="contact">
        <strong>arvenpack.ch</strong><br>
        info@arvenpack.ch<br>
        044 555 12 34
        <div class="owner">Eine Marke von Talberg Medien AG</div>
      </div>
    </div>
  </div>

  <div class="panel panel--navy">
    <div class="badge badge--cover">Mappen,<br>Ordner &amp;<br>mehr</div>
    <div class="cover-photo" role="img" aria-label="Produktfoto: kupferfarbener Schuber und graue Schubladenbox"></div>
    <h1 class="cover-title">High<br>Performance<br>Packaging</h1>
    <p class="cover-sub">Exklusive Verpackungs- und Präsentationslösungen</p>
  </div>
</section>

</body>
</html>
```